Ecommerce Software Provider Needs A Fresh Look For Website

We are looking for a fresh, new look for our existing ecommerce software service. We provide an ecommerce software targeted at small business owners called "QuickelShop" and our existing website can be seen at http://www.quickelshop-example.com.

QuickelShop helps small business owners build their online store instantly without any coding. We focus on not just building "online stores" but PROFITABLE online stores. As such, we focus on tools and features that help our clients create online stores that convert.

The "feel" we want to portray to our clients are as below:

- Powerful
- Easy to use
- Can start quickly
- Successful
- Profitable

We are open to pretty much any color scheme or feel. The only thing we absolutely want to retain is our company logo which uses a shade of green and black.

So, this is pretty much a "free reign" kind of project. Let your imagination and design juices run wild! :-)

Industry/Entity Type

Small Business

```html
<!DOCTYPE html>
<html lang="en">
<head>
<meta charset="utf-8">
<title>QuickelShop – Ecommerce Software</title>
<link href="https://fonts.googleapis.com/css2?family=Yanone+Kaffeesatz:wght@300;400;500;700&family=Open+Sans:wght@400;600;700&display=swap" rel="stylesheet">
<style>
:root{
  --green:#9bc31c;
  --green-dark:#7fa511;
  --green-soft:#e5edbe;
  --green-pale:#f1f4dc;
  --plum:#48293a;
  --panel:#dcdbdc;
  --ink:#4a2a3a;
  --text:#555;
  --rule:#d6d6d6;
  --white:#fff;
}
*{margin:0;padding:0;box-sizing:border-box}
html,body{width:1110px;height:1200px;overflow:hidden;background:var(--white)}
body{font-family:"Open Sans",Arial,sans-serif;color:var(--text);position:relative}

.top-bar{height:18px;background:var(--green);display:flex;justify-content:flex-end;gap:24px;padding-right:34px;align-items:center}
.top-bar a{font-family:"Yanone Kaffeesatz",sans-serif;color:var(--white);font-size:11px;letter-spacing:.6px;text-decoration:none;text-transform:uppercase}

.brand{position:absolute;top:42px;left:0;width:1110px;display:flex;justify-content:center;align-items:center;gap:6px}
.brand-name{font-family:"Open Sans",sans-serif;font-weight:700;font-size:22px;color:#111;letter-spacing:-.3px;text-transform:none}
.brand-dot{width:14px;height:14px;border-radius:50%;background:var(--green)}

.wrap{position:absolute;left:213px;width:685px}

.main-nav{top:92px;height:39px;background:var(--plum);display:flex;justify-content:space-between;align-items:center;padding:0 18px}
.main-nav a{font-family:"Yanone Kaffeesatz",sans-serif;font-size:11.5px;color:#eee;text-decoration:none;letter-spacing:.4px;text-transform:uppercase}
.main-nav a.active{color:var(--green)}

.hero{top:138px;height:221px;display:flex;gap:8px}
.slider{width:454px;height:221px;position:relative;overflow:hidden}
.slide-art{position:absolute;inset:0;background:linear-gradient(180deg,#e98793 0 30px,#f6eee6 30px 60px,#f3e2d8 60px 100%)}
.slide-art::after{content:"";position:absolute;left:65px;top:72px;width:320px;height:140px;background:linear-gradient(90deg,#f3c2c7,#f7e3e0 55%,#f0a9b3)}
.slide-caption{position:absolute;top:108px;left:0;width:454px;height:62px;background:rgba(255,255,255,.55);text-align:center;font-family:"Yanone Kaffeesatz",sans-serif;font-size:21px;line-height:24px;color:var(--green);padding-top:8px;text-transform:uppercase}
.dots{position:absolute;display:flex;gap:4px}
.dots i{display:block;border-radius:50%;background:#ececec;border:1px solid #cfcfcf}
.dots i.on{background:var(--green);border-color:var(--green-dark)}
.slider .dots{right:6px;bottom:4px}
.slider .dots i{width:11px;height:11px}

.latest{width:223px;height:221px;background:var(--panel);position:relative}
.panel-title{font-family:"Yanone Kaffeesatz",sans-serif;font-size:19px;color:var(--green);text-transform:uppercase;letter-spacing:.2px}
.latest .panel-title{text-align:center;padding-top:5px}
.latest-shot{position:absolute;left:27px;top:30px;width:171px;height:170px;background:linear-gradient(180deg,#2d2d2d 0 14px,#f4f4f4 14px);box-shadow:0 1px 4px rgba(0,0,0,.3)}
.latest .dots{left:100px;bottom:6px}
.latest .dots i{width:7px;height:7px}

.features{top:368px;height:164px;display:flex;gap:8px}
.feature{width:223px;height:164px;background:var(--panel);padding:14px 18px 0;position:relative}
.feature-img{margin-top:4px;width:186px;height:55px}
.feature p{font-size:8px;line-height:12px;color:#555;margin-top:12px}
.btn-small{position:absolute;right:22px;bottom:11px;background:var(--green);color:var(--white);font-size:5.5px;padding:2px 7px;border-radius:2px;box-shadow:0 1px 0 var(--green-dark)}

.what-we-do{top:539px;height:174px;background:var(--green);overflow:hidden}
.what-we-do h2{position:absolute;left:18px;top:14px;font-family:"Yanone Kaffeesatz",sans-serif;font-weight:400;font-size:27px;color:var(--white);text-transform:uppercase}
.what-we-do p{position:absolute;left:18px;top:55px;width:315px;font-size:9.2px;line-height:14px;color:#eef5d2}
.btn-plum{position:absolute;left:268px;top:132px;background:var(--plum);color:var(--white);font-size:8.5px;padding:5px 12px;border-radius:3px;border:1px solid #fff6}
.template-stack{position:absolute;left:350px;top:0;width:335px;height:174px;background:linear-gradient(120deg,rgba(155,195,28,0) 0 12%,#2f7d7a 12% 20%,#e98f7c 20% 30%,#f3c3b0 30% 40%,#f4dcd8 40% 100%)}

.why{top:722px;width:270px}
.section-title{font-family:"Yanone Kaffeesatz",sans-serif;font-weight:500;font-size:27px;color:var(--ink);text-transform:uppercase}
.why ul{list-style:none;margin-top:18px}
.why li{font-family:"Yanone Kaffeesatz",sans-serif;font-size:12px;color:#6b5a63;text-transform:uppercase;height:23.1px;line-height:22px;border-bottom:1px dotted var(--rule);padding-left:16px;position:relative;letter-spacing:.2px;white-space:nowrap}
.why li::before{content:"";position:absolute;left:0;top:8px;width:7px;height:7px;border-radius:50%;background:var(--green)}
.why li:last-child{border-bottom:none}
.divider{position:absolute;left:500px;top:726px;width:1px;height:260px;background:#e6e6e6}

.testimonials{top:722px;left:513px;width:385px}
.testimonial{height:69px;display:flex;gap:7px;padding:7px;position:relative;background:var(--green-soft)}
.testimonial + .testimonial{margin-top:7px}
.testimonial.alt{background:var(--green-pale)}
.testimonials .list{margin-top:19px}
.avatar{width:58px;height:55px;border:2px solid var(--white);flex:none}
.testimonial h3{font-family:"Yanone Kaffeesatz",sans-serif;font-weight:400;font-size:11.5px;color:var(--ink);text-transform:uppercase;margin-top:1px}
.testimonial p{font-size:7.6px;line-height:11.5px;color:var(--green-dark);margin-top:3px}
.testimonial .more{position:absolute;right:12px;bottom:6px;font-size:6px;color:#b79e6a}

.footer{position:absolute;left:0;top:1006px;width:1110px;height:186px;background:var(--plum)}
.footer-bottom{position:absolute;left:0;top:1192px;width:1110px;height:8px;background:var(--green)}
.footer .col{position:absolute;top:14px;font-family:"Yanone Kaffeesatz",sans-serif;color:#c9bcc3;font-size:10px;line-height:14px;text-transform:uppercase}
.footer h4{font-weight:400;font-size:16px;color:var(--white);margin-bottom:6px;line-height:18px}
.footer .brand-inline{display:flex;align-items:center;gap:5px;margin-bottom:6px;margin-top:2px}
.footer .brand-inline .brand-name{color:var(--white);font-size:18px}
.footer .body-text{text-transform:none;font-size:10.5px;line-height:14px;text-align:justify}
.footer .legal{text-transform:uppercase;font-size:9.5px;line-height:14px;text-align:justify}
.social{display:flex;gap:3px;margin-top:3px}
.social i{width:10px;height:10px;border-radius:50%;background:#b8a8b1;display:block}
.services li{list-style:none;line-height:21px}
</style>
</head>
<body>

<div class="top-bar">
  <a href="#">Merchant Login</a><a href="#">Signup Now</a><a href="#">Free Trial</a>
</div>

<header class="brand">
  <span class="brand-name">QuickelShop</span><span class="brand-dot"></span>
</header>

<nav class="wrap main-nav">
  <a class="active" href="#">Home</a><a href="#">Cart Features</a><a href="#">Pricing</a><a href="#">Credit Cards</a><a href="#">Happy Clients!</a><a href="#">Ecommerce Templates</a><a href="#">Live Chat</a><a href="#">E-Blog</a><a href="#">Contact</a>
</nav>

<section class="wrap hero">
  <div class="slider">
    <div class="slide-art" role="img" aria-label="Screenshot of a pink cake-decorating online store template"></div>
    <div class="slide-caption">The easiest possible way to get a visitor's<br>attention and improve conversion.</div>
    <div class="dots"><i class="on"></i><i></i><i></i><i></i></div>
  </div>
  <aside class="latest">
    <div class="panel-title">Latest Templates</div>
    <div class="latest-shot" role="img" aria-label="Screenshot of a computer-store template with product grid"></div>
    <div class="dots"><i class="on"></i><i></i><i></i><i></i></div>
  </aside>
</section>

<section class="wrap features">
  <article class="feature">
    <div class="panel-title">Beautiful Templates</div>
    <div class="feature-img" role="img" aria-label="Preview of a store template with a blue fabric banner" style="background:linear-gradient(180deg,#3a3a3a 0 10px,#ffffff 10px 16px,#2f4fa8 16px,#9cb2e0)"></div>
    <p>Lorem ipsum dolor sit amet, consectetur adipi-scing elit. Nunc porttitor, lacus et aliquam ve-hicula, nibh nisi varius mire.</p>
    <span class="btn-small">Read more</span>
  </article>
  <article class="feature">
    <div class="panel-title">Accept Payments Easily</div>
    <div class="feature-img" role="img" aria-label="Photo of a fan of colourful payment cards" style="background:linear-gradient(100deg,#5d8fc9,#c9d6e8 40%,#e2b04a 65%,#c85a4a)"></div>
    <p>Lorem ipsum dolor sit amet, consectetur adipi-scing elit. Nunc porttitor, lacus et aliquam ve-hicula, nibh nisi varius mire.</p>
    <span class="btn-small">Read more</span>
  </article>
  <article class="feature">
    <div class="panel-title">Sell on Friendbook</div>
    <div class="feature-img" role="img" aria-label="Shopping cart illustration on a blue social network banner" style="background:linear-gradient(90deg,#dfe4ee,#3b5a9a)"></div>
    <p>Lorem ipsum dolor sit amet, consectetur adipi-scing elit. Nunc porttitor, lacus et aliquam ve-hicula, nibh nisi varius mire.</p>
    <span class="btn-small">Read more</span>
  </article>
</section>

<section class="wrap what-we-do">
  <h2>What we do.....</h2>
  <p>Lorem ipsum dolor sit amet, consectetur adipiscing elit. Nunc porttitor, lacus et aliquam vehicula, nibh nisi varius mi, in varius tellus enim in leo. Vivamus nec ante neque. Quisque ullamcorper augue et sagittis dignissim. Phasellus consequat insum leo, ac viverra urna dictum nec. Morbi vitae tempus magna.</p>
  <span class="btn-plum">Read more</span>
  <div class="template-stack" role="img" aria-label="Fanned stack of colourful store template screenshots"></div>
</section>

<section class="wrap why">
  <h2 class="section-title">Why Us</h2>
  <ul>
    <li>Lorem ipsum dolor sit amet</li>
    <li>Consectetur adipiscing elit vestibulum tristique</li>
    <li>Vitae duieget varius</li>
    <li>Crassedest non arcu rutrum accumsan</li>
    <li>Utneportaminon sodales velit maurisvitae convallis elit</li>
    <li>Vivamus tortor semsuscipit</li>
    <li>Laoreet venenatis inmattis a libero.</li>
    <li>Ututdig nissimjusto</li>
    <li>Vivamus cursus minisivel porttitorante sagittiseu.</li>
    <li>Crasa congue turpis</li>
  </ul>
</section>
<div class="divider"></div>

<section class="wrap testimonials">
  <h2 class="section-title">Testimonials</h2>
  <div class="list">
    <article class="testimonial">
      <div class="avatar" role="img" aria-label="Customer portrait" style="background:linear-gradient(180deg,#6aa0d8,#3c4f6a)"></div>
      <div><h3>Lorem ipsum dolor sit amet</h3><p>Lorem ipsum dolor sit amet, consectetur adipiscing elit. Nunc porttitor, lacus et aliquam vehicula, nibh nisi varius mi, in varius tellus enim in leo.</p></div>
      <span class="more">Read more</span>
    </article>
    <article class="testimonial alt">
      <div class="avatar" role="img" aria-label="Customer portrait" style="background:linear-gradient(180deg,#c9a36a,#5e9a45)"></div>
      <div><h3>Lorem ipsum dolor sit amet</h3><p>Lorem ipsum dolor sit amet, consectetur adipiscing elit. Nunc porttitor, lacus et aliquam vehicula, nibh nisi varius mi, in varius tellus enim in leo.</p></div>
      <span class="more">Read more</span>
    </article>
    <article class="testimonial">
      <div class="avatar" role="img" aria-label="Customer portrait" style="background:linear-gradient(180deg,#efe3dc,#7a4a36)"></div>
      <div><h3>Lorem ipsum dolor sit amet</h3><p>Lorem ipsum dolor sit amet, consectetur adipiscing elit. Nunc porttitor, lacus et aliquam vehicula, nibh nisi varius mi, in varius tellus enim in leo.</p></div>
      <span class="more">Read more</span>
    </article>
  </div>
</section>

<footer class="footer">
  <div class="col" style="left:213px;width:185px">
    <div class="brand-inline"><span class="brand-name">QuickelShop</span><span class="brand-dot"></span></div>
    <div class="legal">© Copyright 2001-2014 Norvale Systems Sdn. Bhd. All rights reserved. QuickelShop is a registered trademark of Norvale Systems Sdn. Bhd. View privacy policy</div>
    <div class="legal" style="margin-top:6px">Ecommerce software, ecommerce solutions &amp; QuickelShop shopping cart software provider</div>
    <div style="margin-top:6px;font-size:9.5px">Follow us</div>
    <div class="social"><i></i><i></i><i></i><i></i><i></i></div>
  </div>
  <div class="col" style="left:413px;width:140px">
    <h4>Conact Us</h4>
    Norvale Systems Sdn. Bhd.<br>4th Floor Lintang Tower<br>12 Jalan Merbau<br>10200 Penang<br>Malaysia
    <div style="margin-top:12px;line-height:12.5px">Telephone: +60-4-555-0142<br>Facsimile: +60-4-555-0143<br>USA: +1-555-014-2278<br>Australia: +61-3-5550-1987</div>
  </div>
  <div class="col" style="left:563px;width:214px">
    <h4>Shopping Cart Features</h4>
    <div class="body-text">QuickelShop has plenty of shopping cart features that help you make more money online more quickly. Actually, QuickelShop is much more than just a shopping cart with some bells and whistles tacked on. It's a complete and full-featured ecommerce solution that includes a powerful shopping cart o, no matter whether you're looking for shopping cart features like real-time shipping calculation integrated with ParcelOne, SwiftPost &amp; AirCrate or a discount coupon feature, we've got you covered.</div>
  </div>
  <div class="col" style="left:809px;width:110px">
    <h4>Services</h4>
    <ul class="services" style="margin-top:-4px">
      <li>Accept credit cards</li><li>Payment gateways</li><li>Logo design</li><li>Ecommerce web design</li><li>Free live chat software</li><li>Shopping portal</li>
    </ul>
  </div>
</footer>
<div class="footer-bottom"></div>

</body>
</html>
```